Modern Billboard Ad for Criminal Defense Firm

10.5 x 36 We're looking for something to set us apart from the local competition. Looking for sleek and modern. We're a mid-sized firm in a small market city. We want to give the artist room to be creative on this one.
Thanks

Target Market(s)

Adult clients who have been charged with a crime/DWI

Industry/Entity Type

legal

Font styles to use
Serif
Sans Serif

Requirements
Must have
• Needs to have the firm name in large lettering. Law Offices of Marcus T Whitfield. “PLLC” does not have to be included. Phone number of (555) 384-1927 should be included but not the main focus.
Nice to have
• A call to action or something similar. “Don’t go it alone, call today.”, “ Arrested?”

```html
<!DOCTYPE html>
<html lang="en">
<head>
<meta charset="utf-8">
<title>Law Offices of Marcus T Whitfield — Billboard</title>
<link rel="stylesheet" href="https://fonts.googleapis.com/css2?family=Playfair+Display:wght@700;900&family=Questrial&family=Roboto:wght@500;700&family=Roboto+Condensed:wght@700&display=swap">
<style>
  :root {
    --page: #e6e6e6;
    --paper-light: #f7f7f7;
    --paper-mid: #dcdcdc;
    --ink: #111111;
    --band-grey: #4f4f4f;
    --band-black: #1c1c1c;
    --white: #ffffff;
    --badge-blue: #2ba6df;
    --badge-dark: #222222;
    --photo-light: #9a9a9a;
    --photo-dark: #3a3a3a;
  }
  * { margin: 0; padding: 0; box-sizing: border-box; }
  html, body { width: 1200px; height: 1011px; overflow: hidden; background: var(--page); }
  .billboard {
    position: absolute; left: 0; top: 329px;
    width: 1200px; height: 353px; overflow: hidden;
    background: var(--paper-light);
  }
  .backdrop {
    position: absolute; inset: 0;
    background: linear-gradient(100deg, var(--paper-light) 0%, #ececec 35%, var(--paper-mid) 60%, #bdbdbd 100%);
  }
  .portrait {
    position: absolute; left: 615px; top: 0; width: 585px; height: 270px;
    background: radial-gradient(ellipse at 68% 45%, var(--photo-light) 0%, #6e6e6e 45%, var(--photo-dark) 100%);
  }
  .firm-name {
    position: absolute; left: 37px; top: 20px;
    font-family: "Playfair Display", serif; color: var(--ink); white-space: nowrap;
  }
  .firm-name .lead {
    display: block; font-weight: 700; font-size: 50px; line-height: 56px; letter-spacing: 0.5px;
  }
  .firm-name .surname {
    display: block; font-weight: 900; font-size: 84px; line-height: 92px; letter-spacing: -1px;
  }
  .rule {
    position: absolute; left: 37px; top: 269px; width: 483px; height: 2px; background: var(--ink);
  }
  .tagline {
    position: absolute; left: 37px; top: 291px;
    font-family: "Questrial", sans-serif; font-size: 30px; color: var(--ink); white-space: nowrap;
  }
  .cta-band { position: absolute; left: 0; top: 270px; width: 1200px; height: 83px; }
  .cta-band svg { position: absolute; inset: 0; }
  .arrested {
    position: absolute; left: 533px; top: 270px; height: 83px; line-height: 83px;
    font-family: "Roboto Condensed", sans-serif; font-weight: 700; font-size: 60px; color: var(--white);
  }
  .phone {
    position: absolute; left: 895px; top: 270px; height: 83px;
    display: flex; align-items: center; gap: 10px;
    font-family: "Roboto", sans-serif; font-weight: 500; font-size: 31px; color: var(--white); white-space: nowrap;
  }
  .award-badge { position: absolute; left: 625px; top: 23px; width: 157px; height: 229px; }
</style>
</head>
<body>
  <section class="billboard">
    <div class="backdrop" role="img" aria-label="Faint photo of handcuffs on light wood surface"></div>
    <div class="portrait" role="img" aria-label="Black and white portrait of the attorney in vest and tie against wood paneling"></div>

    <svg class="award-badge" viewBox="0 0 157 229" aria-hidden="true">
      <rect x="0" y="0" width="157" height="229" fill="var(--badge-blue)"/>
      <rect x="5" y="5" width="147" height="188" fill="var(--badge-dark)"/>
      <rect x="5" y="5" width="147" height="45" fill="var(--badge-blue)" opacity="0.85"/>
    </svg>

    <h1 class="firm-name">
      <span class="lead">LAW OFFICES OF</span>
      <span class="surname">MARCUS T</span>
      <span class="surname">WHITFIELD</span>
    </h1>
    <div class="rule"></div>

    <div class="cta-band">
      <svg viewBox="0 0 1200 83" width="1200" height="83" aria-hidden="true">
        <rect x="520" y="0" width="680" height="83" fill="var(--band-grey)"/>
        <polygon points="880,0 1200,0 1200,83 831,83" fill="var(--band-black)"/>
      </svg>
    </div>
    <p class="tagline">Don’t go it alone, call today.</p>
    <p class="arrested">ARRESTED?</p>
    <p class="phone">
      <svg width="30" height="30" viewBox="0 0 30 30" aria-hidden="true">
        <circle cx="15" cy="15" r="13" fill="none" stroke="var(--white)" stroke-width="2.2"/>
        <path d="M10.5 8.5c.8-.6 1.6-.4 2 .3l1.3 2.3c.4.7.2 1.4-.4 1.8l-.8.5c.6 1.6 1.9 3 3.5 3.7l.5-.8c.4-.6 1.1-.8 1.8-.4l2.3 1.3c.7.4.9 1.2.3 2-.9 1.3-2.3 1.9-3.8 1.3-3.4-1.3-6-3.9-7.3-7.3-.6-1.5 0-2.9.6-3.7z" fill="var(--white)"/>
      </svg>
      (555) 384-1927
    </p>
  </section>
</body>
</html>
```